New Business Card

Would like a shiny card with Metallic logo raised on th front. Address 418 Kestwick Lane, Toronto Ontario M4T2B8, phone 416 555 0382, email kmvc@lorentel.ca and web www.kmvc.ca on the back in right and left lower corners balanced. Top of back should say Personalized Care for Pet's and their People centered. Leaving space on the back to write. Horizontal placement

```html
<!DOCTYPE html>
<html lang="en">
<head>
<meta charset="utf-8">
<title>Kestwick Meadow Veterinary Clinic – Business Card</title>
<link rel="stylesheet" href="https://fonts.googleapis.com/css2?family=Open+Sans:wght@400;600;700&display=swap">
<style>
  :root {
    --backdrop: #ece7e1;
    --kraft: #c3a680;
    --kraft-light: #cdb28d;
    --kraft-dark: #b89a72;
    --cream: #f7e8da;
    --ink: #141210;
    --rule: #5a4a38;
  }
  * { box-sizing: border-box; margin: 0; padding: 0; }
  html, body {
    width: 1200px;
    height: 900px;
    overflow: hidden;
    background: var(--backdrop);
    font-family: "Open Sans", Arial, sans-serif;
    color: var(--ink);
  }
  .canvas { position: relative; width: 1200px; height: 900px; }

  .card {
    position: absolute;
    background: linear-gradient(160deg, var(--kraft-light), var(--kraft) 50%, var(--kraft-dark));
    box-shadow: 0 4px 14px rgba(0,0,0,0.18);
    overflow: hidden;
  }

  /* Back of card */
  .card-back { left: 238px; top: 62px; width: 555px; height: 342px; }
  .tagline-band {
    height: 62px;
    display: flex;
    align-items: center;
    justify-content: center;
  }
  .tagline { font-size: 16px; font-weight: 600; }
  .writing-space { height: 111px; background: var(--cream); }
  .contact {
    text-align: center;
    font-size: 15.5px;
    line-height: 23px;
    padding-top: 26px;
  }
  .contact-label { font-weight: 700; }
  .contact-rule {
    width: 84px;
    height: 1px;
    background: var(--rule);
    margin: 8px auto 8px;
  }

  /* Front of card */
  .card-front { left: 457px; top: 518px; width: 560px; height: 344px; }
  .brand {
    position: absolute;
    inset: 0;
    display: flex;
    flex-direction: column;
    align-items: center;
    justify-content: center;
    gap: 22px;
    padding-top: 10px;
  }
  .brand-mark {
    width: 110px;
    height: 110px;
    border-radius: 50%;
    background: var(--ink);
  }
  .brand-name {
    font-weight: 600;
    text-align: center;
    text-transform: uppercase;
    letter-spacing: 2px;
    line-height: 1.2;
  }
  .brand-name-main { display: block; font-size: 32px; }
  .brand-name-sub { display: block; font-size: 17px; letter-spacing: 4px; }
</style>
</head>
<body>
<main class="canvas">
  <section class="card card-back" aria-label="Business card back">
    <div class="tagline-band">
      <p class="tagline">Personalized Care for Pet's and their People</p>
    </div>
    <div class="writing-space"></div>
    <div class="contact">
      <p><span class="contact-label">P</span>: 416 555 0382</p>
      <p><span class="contact-label">E</span>: kmvc@lorentel.ca</p>
      <p><span class="contact-label">W</span>: www.kmvc.ca</p>
      <div class="contact-rule"></div>
      <p>418 Kestwick Lane,</p>
      <p>Toronto Ontario M4T2B8</p>
    </div>
  </section>

  <section class="card card-front" aria-label="Business card front">
    <div class="brand">
      <div class="brand-mark"></div>
      <p class="brand-name">
        <span class="brand-name-main">Kestwick Meadow</span>
        <span class="brand-name-sub">Veterinary Clinic</span>
      </p>
    </div>
  </section>
</main>
</body>
</html>
```